Social Business Consultancy

Kavora Ventures is a start up consultancy but with a difference: were non-corporate. We work in the field of economic development in low income countries and we focus on entrepreneurship but with a social and or environmental mission.

The type of projects we work on are innovative, ground breaking, different, edgy and bold. We are young, determined, , unreasonnable and undeterred by challenges.
We want our website to convey these ideas.
Updates

Hello,

Could you please include the option of having the website in two languages. Thank you.

Please note that new files have been added to the project brief.

- FrontPage  Main Photo (Grey dirt Road)
- WordCloud Photo to be used on the home page (as a small image )

The website should keep these colour tones.

Thank you !

Hello,

Wireframes have been uploaded. Please use as an indication.

Thanks,
n.

Target Market(s)

Governments, development agencies, social investors, NGOs, banks and social entrepreneurs.

Industry/Entity Type

Consulting

Requirements
Must have
• We already have a logo and business cards (provided). We want the website to look professional, yet simple with a maximum of two or three colours. We want the look to be seamless. There is no need for too many boxes or categories.
Nice to have
• We want bold, edgy, modern  and professional look .
• Examples:
• http://www.brightmarrowlab.org/
• http://www.pavelstone.com/
• http://www.tarnhiring.co.nz/
Should not have
• The design should not use old style fonts.

```html
<!DOCTYPE html>
<html lang="en">
<head>
<meta charset="utf-8">
<title>Kavora Ventures — Social Business Initiatives</title>
<link rel="stylesheet" href="https://fonts.googleapis.com/css2?family=Questrial&display=swap">
<style>
  :root{
    --ink:#5d5d5d;
    --text:#6a6a6a;
    --sky:#1aa3e8;
    --sky-bright:#00aeef;
    --lime:#b5cc18;
    --lime-soft:#d9e57c;
    --lime-hero:#c0d12f;
    --orange:#f26522;
    --orange-soft:#f7a57e;
    --grey-dark:#5f6062;
    --grey-frame:#a9aaab;
    --nav-top:#8a8b8c;
    --nav-bottom:#5b5c5e;
    --rule:#b3b3b3;
    --white:#ffffff;
  }
  *{box-sizing:border-box;margin:0;padding:0}
  html,body{width:1200px;height:1095px;overflow:hidden;background:var(--white)}
  body{position:relative;font-family:"Questrial",sans-serif;color:var(--text)}
  .abs{position:absolute}

  .quick-links{left:32px;top:57px;display:flex;gap:16px}
  .quick-link{width:35px;height:35px;border:1px solid #b9b9b9;border-radius:4px;
    background:linear-gradient(#fafafa,#d9d9d9);display:flex;align-items:center;justify-content:center}

  .main-nav{left:29px;top:115px;width:750px;height:80px;border:1px solid #7c7d7e;
    background:linear-gradient(var(--nav-top),var(--nav-bottom) 60%,#6d6e70);
    display:flex;align-items:center;padding-left:55px;color:var(--white);font-size:20px;letter-spacing:.5px}
  .main-nav a{color:inherit;text-decoration:none}
  .main-nav .sep{margin:0 40px}

  .brand{left:917px;top:32px;width:260px;text-align:right}
  .brand-name{font-size:84px;line-height:1;color:var(--ink);display:flex;align-items:center;justify-content:flex-end;gap:10px}
  .brand-mark{width:70px;height:70px;background:var(--lime);display:inline-block}
  .brand-tag{margin-top:22px;font-size:18px;color:var(--ink)}

  .hero{left:31px;top:217px;width:748px;height:376px;border:6px solid var(--lime-soft);
    background:radial-gradient(circle at 45% 45%,#d8e27a 0,var(--lime-hero) 45%,#b7c926 100%)}

  .dash-v{border-left:2px dashed var(--rule)}

  .side-head{width:353px;height:84px;border:1px solid #9a9a9a;border-left-width:12px;display:flex;align-items:center;background:var(--white)}
  .side-head.news{border-left-color:var(--grey-dark)}
  .side-head.events{border-left-color:var(--lime)}
  .side-head h2{font-weight:400;font-size:32px;color:var(--sky)}
  .side-text{font-size:15.5px;line-height:27px;color:var(--text);width:310px}
  .read-more{font-size:16px;color:var(--orange);text-decoration:none}

  .section-title{font-weight:400;color:var(--sky)}
  .section-rule{height:1px;background:#9b9b9b}
  .welcome-copy{left:38px;top:694px;width:345px;font-size:15.5px;line-height:27.6px;text-align:justify}
  .service-list{left:443px;top:692px;list-style:none;font-size:15.5px}
  .service-list li{height:30px;display:flex;align-items:center;gap:31px}
  .bullet{width:10px;height:10px;background:var(--grey-dark)}
  .bullet.lime{background:var(--lime)}

  .promo{top:879px;height:93px;border:4px solid}
  .promo.subscribe{left:31px;width:369px;background:var(--orange);border-color:var(--orange-soft)}
  .promo.about{left:410px;width:368px;background:var(--sky-bright);border-color:#7fd4f7;
    display:flex;align-items:center;color:var(--white);font-size:28px}
  .promo.call{left:790px;width:386px;background:var(--grey-dark);border-color:var(--grey-frame);
    display:flex;align-items:center;color:var(--white);font-size:28px;padding-left:43px}
  .email-field{position:absolute;left:95px;top:35px;width:218px;height:32px;border:1px solid #999;
    background:var(--white);font-size:16px;color:#444;padding:5px 6px}

  .footer-rule{left:207px;top:1007px;width:770px;border-top:2px dashed var(--rule)}
  .footer{left:0;top:1036px;width:1208px;text-align:center;font-size:14.5px;color:#444}
  .footer .site{color:var(--sky)}
</style>
</head>
<body>

<div class="abs quick-links">
  <span class="quick-link" title="Home"><svg width="22" height="20" viewBox="0 0 22 20"><path d="M2 10 11 2l9 8M5 8v10h12V8" fill="none" stroke="#777" stroke-width="1.6"/><rect x="9" y="12" width="4" height="6" fill="#777"/></svg></span>
  <span class="quick-link" title="Mail"><svg width="22" height="16" viewBox="0 0 22 16"><rect x="1" y="1" width="20" height="14" fill="none" stroke="#777" stroke-width="1.6"/><path d="M1 1l10 8 10-8" fill="none" stroke="#777" stroke-width="1.6"/></svg></span>
  <span class="quick-link" title="Sitemap"><svg width="22" height="20" viewBox="0 0 22 20"><rect x="7" y="1" width="8" height="6" fill="none" stroke="#777" stroke-width="1.5"/><path d="M11 7v4M4 11h14M4 11v3M11 11v3M18 11v3" stroke="#777" stroke-width="1.5"/><rect x="1" y="14" width="6" height="5" fill="#777"/><rect x="8" y="14" width="6" height="5" fill="#777"/><rect x="15" y="14" width="6" height="5" fill="#777"/></svg></span>
</div>

<nav class="abs main-nav">
  <a href="#">About</a><span class="sep">|</span>
  <a href="#">Welcome</a><span class="sep">|</span>
  <a href="#">Our Services</a><span class="sep">|</span>
  <a href="#">Contact Us</a>
</nav>

<div class="abs brand">
  <div class="brand-name" style="font-size:62px">Kavora <span class="brand-mark"></span></div>
  <div class="brand-tag">Social Business Initiatives</div>
</div>

<div class="abs hero" role="img" aria-label="Word cloud of social business themes around a fingerprint with the company name and the line Be part of the Change"></div>

<div class="abs dash-v" style="left:802px;top:217px;height:613px"></div>

<div class="abs side-head news" style="left:824px;top:217px">
  <svg width="60" height="60" viewBox="0 0 60 60" style="margin:0 20px 0 16px"><circle cx="30" cy="30" r="27" fill="#dcdcdc"/><circle cx="30" cy="30" r="21" fill="var(--orange)"/><circle cx="22" cy="38" r="3.5" fill="#fff"/><path d="M20 27a11 11 0 0 1 11 11M20 19a19 19 0 0 1 19 19" fill="none" stroke="#fff" stroke-width="3.5"/></svg>
  <h2>Our News</h2>
</div>
<p class="abs side-text" style="left:859px;top:324px">Lorem Ipsum is simply dummy text of the printing and typesetting industry.</p>
<p class="abs side-text" style="left:859px;top:402px">Lorem Ipsum is simply dummy text of the printing and typesetting industry.</p>
<a class="abs read-more" href="#" style="left:1074px;top:484px">Read More...</a>

<div class="abs side-head events" style="left:824px;top:515px">
  <svg width="66" height="66" viewBox="0 0 66 66" style="margin:0 36px 0 14px"><rect x="6" y="10" width="52" height="50" rx="3" fill="#fff" stroke="#999" stroke-width="2"/><rect x="6" y="10" width="52" height="16" fill="#c8202b"/><circle cx="20" cy="8" r="3" fill="#555"/><circle cx="44" cy="8" r="3" fill="#555"/><text x="32" y="52" text-anchor="middle" font-family="Questrial,sans-serif" font-size="24" fill="#333">17</text><text x="32" y="23" text-anchor="middle" font-family="Questrial,sans-serif" font-size="10" fill="#fff">JUL</text></svg>
  <h2>Events</h2>
</div>
<p class="abs side-text" style="left:859px;top:621px">Lorem Ipsum is simply dummy text of the printing and typesetting industry.</p>
<p class="abs side-text" style="left:856px;top:711px">Lorem Ipsum is simply dummy text of the printing and typesetting industry.</p>
<a class="abs read-more" href="#" style="left:1070px;top:829px">Read More...</a>

<svg class="abs" style="left:32px;top:621px" width="58" height="58" viewBox="0 0 58 58"><circle cx="29" cy="29" r="27" fill="#e6e6e6" stroke="#c7c7c7"/><path d="M29 29V8a21 21 0 0 1 19 28z" fill="#f7941d"/><path d="M29 29l19 7A21 21 0 0 1 12 42z" fill="#8dc63f"/><path d="M29 29 12 42A21 21 0 0 1 29 8z" fill="#27aae1"/></svg>
<h2 class="abs section-title" style="left:102px;top:626px;font-size:39px">Welcome</h2>
<div class="abs section-rule" style="left:102px;top:678px;width:217px"></div>
<p class="abs welcome-copy">Lorem Ipsum is simply dummy text of the printing and typesetting industry. Lorem Ipsum has been the industry's standard dummy text ever since the 1500s, when an unknown printer took a galley of type and scrambled it to make a type specimen book.</p>
<a class="abs read-more" href="#" style="left:282px;top:847px">Read More...</a>

<div class="abs dash-v" style="left:411px;top:626px;height:217px"></div>

<svg class="abs" style="left:438px;top:623px" width="57" height="57" viewBox="0 0 57 57"><circle cx="28.5" cy="28.5" r="26" fill="#e6e6e6" stroke="#c7c7c7"/><circle cx="28.5" cy="28.5" r="19" fill="#fff"/><path d="M16 40 30 18l3 6-10 16zM26 40l9-14 3 5-5 9zM36 40l4-6 3 6z" fill="#3aa14a"/></svg>
<h2 class="abs section-title" style="left:513px;top:631px;font-size:33px">Services</h2>
<div class="abs section-rule" style="left:513px;top:678px;width:217px"></div>
<ul class="abs service-list">
  <li><span class="bullet"></span>Lorem Ipsum is simply dummy text</li>
  <li><span class="bullet lime"></span>Lorem Ipsum is simply dummy text</li>
  <li><span class="bullet"></span>Lorem Ipsum is simply dummy text</li>
  <li><span class="bullet lime"></span>Lorem Ipsum is simply dummy text</li>
</ul>
<a class="abs read-more" href="#" style="left:678px;top:843px">Read More...</a>

<div class="abs promo subscribe">
  <svg class="abs" style="left:6px;top:16px" width="60" height="54" viewBox="0 0 60 54"><rect x="14" y="4" width="40" height="28" fill="#f9d36b" transform="rotate(10 34 18)"/><rect x="4" y="18" width="44" height="30" fill="#fde6a0" stroke="#e0a930"/><path d="M4 18l22 16 22-16" fill="none" stroke="#e0a930" stroke-width="1.5"/></svg>
  <div class="email-field">Enter your email</div>
  <svg class="abs" style="left:320px;top:35px" width="34" height="34" viewBox="0 0 34 34"><circle cx="17" cy="17" r="15" fill="#555" stroke="#ddd" stroke-width="3"/><path d="M11 12l7 5-7 5zM20 11h3v12h-3z" fill="#fff"/></svg>
</div>
<div class="abs promo about">
  <svg style="margin:0 22px 0 15px" width="62" height="62" viewBox="0 0 62 62"><circle cx="31" cy="31" r="28" fill="#dfe9f3" stroke="#fff" stroke-width="2"/><circle cx="31" cy="31" r="22" fill="#2b7fd0"/><path d="M18 24c6-4 10 2 14 0s4 8 0 10-8 8-12 4-6-10-2-14zM38 38c3-2 6 0 5 4s-5 2-5-4z" fill="#9ad0f5"/></svg>
  About Company
</div>
<svg class="abs" style="left:920px;top:841px" width="92" height="58" viewBox="0 0 92 58"><path d="M86 50C84 22 66 10 40 14" fill="none" stroke="#6fb52c" stroke-width="12"/><path d="M44 0 16 16l26 22z" fill="#6fb52c"/></svg>
<div class="abs promo call">Call Free : 000 000 000</div>

<div class="abs footer-rule"></div>
<footer class="abs footer"><span class="site">kavoraventures.com</span> &nbsp;© 2010 &nbsp;| &nbsp;Privacy Policy &nbsp;| &nbsp;Terms Of use</footer>

</body>
</html>
```